Modern, Sleek & Vibrant design required for electrical contracting work.

I require a flyer design for BRANDEL VOLT SERVICES, which operates as an electrical contractor. We do electrical installations such as LED lighting, maintenance, repairs, communications and various other work related for residential and commercial customers. I would like the same colours applied from my logo to the flyer (Electric Blue, White, Grey/Silver). A6 or DL sizes with single side.

Target Market(s)

Residential and Commercial customers.

Industry/Entity Type

Communications

Font styles to use
Serif
Sans Serif

Requirements
Must have
• My logo and colours (Electric Blue, White, Silver/Grey)
Nice to have
• Shapes separating different parts of the flyer, such as the same electric bolt from my logo. Straight or angled shapes.
Should not have
• Childish pictures such as light bulbs. Curved shapes.

```html
<!DOCTYPE html>
<html lang="en">
<head>
<meta charset="utf-8">
<title>Brandel Volt Services – Flyer</title>
<link rel="stylesheet" href="https://fonts.googleapis.com/css2?family=Exo+2:wght@400;600;700;800&display=swap">
<style>
  :root {
    --backdrop: #3a3b3d;
    --paper: #ffffff;
    --electric-blue: #2f4db5;
    --navy-deep: #061426;
    --navy-band: #0b2a4a;
    --bokeh-light: #cfe4f6;
    --bokeh-mid: #5f9fd6;
    --bokeh-dark: #123a63;
    --ink-black: #0a0d12;
    --tile-dark: #0c1420;
    --tile-navy: #0d2a47;
    --tile-teal: #0e5f8c;
    --silver: #c9ccd1;
    --silver-dim: #a7abb2;
    --white: #ffffff;
  }
  * { box-sizing: border-box; margin: 0; padding: 0; }
  html, body {
    width: 1052px; height: 1200px; overflow: hidden;
    background: var(--backdrop);
    font-family: "Exo 2", sans-serif;
  }
  .flyer {
    position: absolute; left: 136px; top: 50px;
    width: 780px; height: 1100px; overflow: hidden;
    background: var(--ink-black);
  }
  .flyer__photo {
    position: absolute; left: 0; top: 160px; width: 100%; height: 820px;
    background:
      radial-gradient(ellipse at 18% 25%, var(--bokeh-light) 0%, transparent 22%),
      radial-gradient(ellipse at 85% 20%, var(--bokeh-light) 0%, transparent 20%),
      radial-gradient(ellipse at 50% 40%, var(--bokeh-mid) 0%, transparent 55%),
      linear-gradient(180deg, var(--bokeh-mid) 0%, var(--bokeh-dark) 55%, var(--ink-black) 100%);
  }
  .flyer__header { position: absolute; left: 0; top: 0; width: 780px; height: 300px; }
  .brand {
    position: absolute; left: 0; top: 58px; width: 100%;
    display: flex; align-items: center; justify-content: center; gap: 18px;
  }
  .brand__dot {
    width: 58px; height: 58px; border-radius: 50%;
    background: var(--electric-blue);
  }
  .brand__name {
    color: var(--electric-blue); font-weight: 800; font-size: 50px;
    letter-spacing: 1px; line-height: 1;
  }
  .services {
    position: absolute; left: 179px; top: 327px; width: 423px;
    list-style: none;
  }
  .services__item {
    height: 68px; margin-bottom: 22px;
    display: flex; align-items: center; justify-content: center;
    color: var(--white); font-weight: 800; font-size: 32px; letter-spacing: 0.5px;
    box-shadow: 4px 6px 10px rgba(0,0,0,0.45);
  }
  .services__item--dark { background: var(--tile-dark); }
  .services__item--navy { background: var(--tile-navy); }
  .services__item--teal { background: var(--tile-teal); }
  .contact {
    position: absolute; left: 0; top: 918px; width: 100%; text-align: center;
  }
  .contact__name { color: var(--silver); font-weight: 700; font-size: 33px; line-height: 1.1; }
  .contact__role { color: var(--silver-dim); font-weight: 400; font-size: 22px; line-height: 1; }
  .contact__email {
    margin-top: 42px; display: flex; align-items: center; justify-content: center; gap: 16px;
    color: var(--silver); font-size: 27px; font-weight: 400;
  }
</style>
</head>
<body>
  <main class="flyer">
    <div class="flyer__photo" role="img" aria-label="Blurred blue bokeh of bright stadium-style lights"></div>

    <svg class="flyer__header" viewBox="0 0 780 300" aria-hidden="true">
      <path d="M0,230 C120,250 260,262 420,236 C560,214 680,185 780,170 V235 C660,250 540,290 400,300 C250,306 110,292 0,278 Z" fill="var(--navy-band)"/>
      <path d="M0,230 C140,262 300,262 430,232 C560,204 680,180 780,170 V195 C660,205 540,245 410,268 C260,290 110,280 0,262 Z" fill="var(--navy-deep)"/>
      <path d="M0,0 H780 V170 C680,180 560,204 430,232 C300,260 140,258 0,230 Z" fill="var(--paper)"/>
    </svg>

    <div class="brand">
      <span class="brand__dot"></span>
      <span class="brand__name">BRANDEL VOLT SERVICES</span>
    </div>

    <ul class="services">
      <li class="services__item services__item--dark">LED LIGHTING</li>
      <li class="services__item services__item--dark">INSTALLATIONS</li>
      <li class="services__item services__item--navy">MAINTENANCE</li>
      <li class="services__item services__item--navy">REPAIRS</li>
      <li class="services__item services__item--teal">COMMUNICATIONS</li>
      <li class="services__item services__item--teal">EMERGENCY CALL-OUTS</li>
    </ul>

    <section class="contact">
      <p class="contact__name">Daniel Brandel</p>
      <p class="contact__role">Director</p>
      <p class="contact__email">
        <svg width="38" height="26" viewBox="0 0 38 26" aria-hidden="true">
          <rect x="1" y="1" width="36" height="24" fill="var(--electric-blue)"/>
          <path d="M1,1 L19,15 L37,1" fill="none" stroke="var(--navy-deep)" stroke-width="2"/>
        </svg>
        daniel@brandelvolt.com
      </p>
    </section>
  </main>
</body>
</html>
```